Label for luxury drink/cocktail flavour bags

I need a luxury label designed for our new product, which are infusion bags for drinks and cocktails. We are a saffron producer so all will contain saffron and the name of the product is Velvet Draughts. There will be 10 bags in each pack, and the packaging will be a cardboard cylinder which is 105mm high x 85mm wide. The tagline is "Elevate every pour", and the first variety will be called Gilded Blush. The ingredients are saffron, rose petals and hibiscus flower. The label needs to feel luxurious, and I would like a gold foil element in the final printing so please include that in the design. Our brand is Wexmoor Australian Saffron. I like clean designs, without excessive detail but would be open to some saffron flower illustrations included. The design needs to be editable for different blends as we release them.

Target Market(s)

30-60 year old females with a high income

Industry/Entity Type

Food and drink

Requirements
Must have
• Elevate every pour, Brand, Ingredients section (for this one, Saffron, Rose Petals, Hibiscus Flowers), and one of the attached "made in" marks on the pack

```html
<!DOCTYPE html>
<html lang="en">
<head>
<meta charset="utf-8">
<title>Velvet Draughts – Gilded Blush label</title>
<link rel="stylesheet" href="https://fonts.googleapis.com/css2?family=Montserrat:wght@400;600&family=Mrs+Saint+Delafield&family=Cormorant+Garamond:wght@500&display=swap">
<style>
  :root {
    --page: #ffffff;
    --label: #ececec;
    --label-edge: #e2e2e2;
    --ink: #1d1d1d;
    --gold: #b08d57;
    --gold-dark: #8e6f3e;
    --soft-ink: #555555;
  }
  * { margin: 0; padding: 0; box-sizing: border-box; }
  html, body {
    width: 1200px;
    height: 849px;
    overflow: hidden;
    background: var(--page);
  }
  .canvas {
    position: relative;
    width: 1200px;
    height: 849px;
    display: flex;
    align-items: center;
    justify-content: center;
  }
  .label {
    position: relative;
    width: 460px;
    height: 780px;
    background: var(--label);
    border: 1px solid var(--label-edge);
    display: flex;
    flex-direction: column;
    align-items: center;
    text-align: center;
  }
  .brand {
    margin-top: 150px;
    display: flex;
    align-items: center;
    gap: 8px;
    font-family: "Montserrat", sans-serif;
    font-weight: 600;
    font-size: 9px;
    letter-spacing: 0.32em;
    color: var(--ink);
    text-transform: uppercase;
  }
  .brand-dot {
    width: 6px;
    height: 6px;
    border-radius: 50%;
    background: var(--ink);
  }
  .product-name {
    margin-top: 70px;
    font-family: "Montserrat", sans-serif;
    font-weight: 600;
    font-size: 15px;
    letter-spacing: 0.42em;
    color: var(--gold);
    text-transform: uppercase;
    padding-left: 0.42em;
  }
  .tagline {
    margin-top: 6px;
    font-family: "Montserrat", sans-serif;
    font-weight: 600;
    font-size: 7.5px;
    letter-spacing: 0.4em;
    color: var(--soft-ink);
    text-transform: uppercase;
    padding-left: 0.4em;
  }
  .variety {
    margin-top: 44px;
    font-family: "Mrs Saint Delafield", cursive;
    font-weight: 400;
    font-size: 104px;
    line-height: 0.82;
    color: var(--ink);
  }
  .variety-line { display: block; }
  .variety-line--second { padding-left: 40px; }
  .ingredients {
    margin-top: auto;
    margin-bottom: 118px;
    font-family: "Cormorant Garamond", serif;
    font-weight: 500;
    font-size: 14px;
    line-height: 1.45;
    letter-spacing: 0.03em;
    color: var(--ink);
    text-transform: uppercase;
  }
</style>
</head>
<body>
  <main class="canvas">
    <section class="label" aria-label="Velvet Draughts Gilded Blush label">
      <div class="brand">
        <span class="brand-dot" aria-hidden="true"></span>
        <span class="brand-name">Wexmoor Australian Saffron</span>
      </div>
      <h1 class="product-name">Velvet Draughts</h1>
      <p class="tagline">Elevate every pour</p>
      <h2 class="variety">
        <span class="variety-line">Gilded</span>
        <span class="variety-line variety-line--second">Blush</span>
      </h2>
      <p class="ingredients">Saffron, rose petals<br>and hibiscus flower</p>
    </section>
  </main>
</body>
</html>
```